TeeWiseHub Stationery and Style Guide, You set the tone! (logo Provided)

TeewiseHub is a new and exciting business that will be focusing on providing quality golf information for all Australian golfers.

We already have a great logo and now we are looking to style our documents.

We would like to see the following:

- Front cover page Design including(logo, branding statement and Document title) Branding statement is Every Green - Every Player
- Sales Document design, this is our main document and we would like you to spend most time on this document. I have attached a sample PDF with the basic layout. but you will need to add some flair to the document and make it look great.
- A Dot point design explaining points in an image (I have attached a sample to show what I mean) Please include this image in the Sales Document
- A footnote for all documents(containing, small logo, branding statement and website address)
- An email signature (containing: logo, Dov Hallberg, dov@teewisehub.com.au, 0471 529 318, www.teewisehub.com.au)

The font used in the logo is borisblackboxx.
At this stage we don't need business cards or envelopes please.

A little background:
The service will be providing:

• A Website that allows all Australian golfers to find golf courses close to them on a simple to use Google map
• Browse golf courses on a map or by search.
• View full information about a golf course including images, facilities, prices and full contact details.
• Mobile version of the website for Iphone, Android and other mobile platforms.
• We will use the users GPS location to show them where they are and what golf courses are near them.
• All golf courses will be able to show specials and other deals for all visitors.

Thank you for looking at our project and we look forward to your designs.

Target Market(s)

All Australian Golfers

Industry/Entity Type

Golf Course

Requirements
Must have
• A great Sales Document Design as that is the main stationery document we will be using.
Please use the sample Sales Document for sample content and basic elements needed.
Should not have
• We don't need business cards and envelope design.

```html
<!DOCTYPE html>
<html lang="en">
<head>
<meta charset="utf-8">
<title>TeewiseHub Stationery</title>
<link rel="stylesheet" href="https://fonts.googleapis.com/css2?family=Arimo:wght@400;700&display=swap">
<style>
:root{
  --bg:#ece9e4;
  --paper:#ffffff;
  --green:#8cc63f;
  --green-dark:#5aa02c;
  --orange:#f7941d;
  --grey:#6d6e71;
  --grey-light:#c9cacc;
  --ink:#3a3a3a;
  --label:#ffffff;
  --tee-top:#eeeeee;
  --tee-bottom:#f1d27a;
}
*{margin:0;padding:0;box-sizing:border-box}
html,body{width:1200px;height:561px;overflow:hidden}
body{background:var(--bg);font-family:"Arimo",Arial,sans-serif;position:relative;color:var(--ink)}
.page{position:absolute;top:20px;width:338px;height:438px;background:var(--paper);box-shadow:0 1px 4px rgba(0,0,0,.18);overflow:hidden}
.page--cover{left:43px}
.page--sales{left:426px}
.page--benefits{left:809px}
.page__header{position:absolute;left:0;top:0;width:338px;height:140px}
.brand{position:absolute;left:34px;top:62px;display:flex;align-items:center;gap:4px}
.brand__mark{width:8px;height:8px;border-radius:50%;background:var(--green)}
.brand__name{font-weight:700;font-size:12px;color:var(--ink);letter-spacing:-.2px}
.brand__tagline{position:absolute;left:34px;top:80px;font-size:7px;font-weight:700;color:var(--grey)}
.tee-visual{position:absolute;right:16px;bottom:14px;width:18px;height:36px;background:linear-gradient(var(--tee-top),var(--tee-bottom))}
.page__footer{position:absolute;left:18px;right:18px;bottom:9px;border-top:1px solid var(--grey-light);padding-top:4px;display:flex;justify-content:center;gap:22px;font-size:5px}
.page__footer-tag{font-weight:700;color:var(--grey)}
.page__footer-url{color:var(--green-dark)}
.section-title{position:absolute;left:37px;font-size:8px;font-weight:700;color:var(--orange)}
.body-copy{position:absolute;left:37px;width:258px;font-size:5.6px;line-height:11.5px;color:var(--green)}
.body-copy p{margin-bottom:11px}
.body-copy--column{width:110px;text-align:justify;line-height:8.3px}
.body-copy--column p{margin-bottom:8px}
.body-copy--benefits{line-height:8.3px}
.body-copy--benefits p{margin-bottom:8px}
.bullet-list{list-style:none;margin-bottom:8px}
.bullet-list li{position:relative;padding-left:6px}
.bullet-list li::before{content:"•";position:absolute;left:0}
.phone-visual{position:absolute;left:208px;top:295px;width:50px;height:97px;background:linear-gradient(160deg,#6b7a88,#22272c)}
.callouts{position:absolute;left:168px;top:300px;width:140px;height:80px;overflow:visible}
.callout-label{font-size:3.5px;fill:var(--grey)}
.brand--small{left:34px;top:398px}
.brand--small .brand__name{font-size:10px}
.page-label{position:absolute;top:462px;font-size:10px;color:var(--ink)}
.signature{position:absolute;left:537px;top:470px;width:160px;height:60px;background:var(--paper);box-shadow:0 1px 3px rgba(0,0,0,.18);overflow:hidden}
.signature__band{position:absolute;left:0;top:0}
.signature__name{position:absolute;right:14px;top:6px;font-size:6px;font-weight:700;color:var(--label)}
.signature .brand{left:8px;top:21px}
.signature .brand__mark{width:6px;height:6px}
.signature .brand__name{font-size:8px}
.signature .brand__tagline{left:8px;top:41px;font-size:4.5px}
.signature__contact{position:absolute;right:12px;top:34px;text-align:right;font-size:4.5px;line-height:6px;color:var(--grey)}
.signature-label{position:absolute;left:582px;top:534px;font-size:10px;color:var(--ink)}
</style>
</head>
<body>

<section class="page page--cover">
  <svg class="page__header" viewBox="0 0 338 140" aria-hidden="true">
    <defs>
      <linearGradient id="band1" x1="0" x2="1"><stop offset="0" stop-color="#d4e86a"/><stop offset=".45" stop-color="#8cc63f"/><stop offset="1" stop-color="#6cb33f"/></linearGradient>
    </defs>
    <path d="M0 0H338V100C250 60 150 25 0 6Z" fill="url(#band1)"/>
    <path d="M60 15C170 33 260 72 338 110V122C260 84 170 44 60 15Z" fill="#c9cacc"/>
  </svg>
  <div class="brand"><span class="brand__mark"></span><span class="brand__name">TeewiseHub</span></div>
  <div class="brand__tagline">Every Green - Every Player</div>
  <div class="tee-visual" role="img" aria-label="Golf ball resting on a tee"></div>
  <footer class="page__footer"><span class="page__footer-tag">Every Green - Every Player</span><span class="page__footer-url">www.teewisehub.com.au</span></footer>
</section>

<section class="page page--sales">
  <svg class="page__header" viewBox="0 0 338 140" aria-hidden="true">
    <defs>
      <linearGradient id="band2" x1="0" x2="1"><stop offset="0" stop-color="#d4e86a"/><stop offset=".45" stop-color="#8cc63f"/><stop offset="1" stop-color="#6cb33f"/></linearGradient>
    </defs>
    <path d="M0 0H338V100C250 60 150 25 0 6Z" fill="url(#band2)"/>
    <path d="M60 15C170 33 260 72 338 110V122C260 84 170 44 60 15Z" fill="#c9cacc"/>
  </svg>
  <div class="brand"><span class="brand__mark"></span><span class="brand__name">TeewiseHub</span></div>
  <div class="brand__tagline">Every Green - Every Player</div>
  <h2 class="section-title" style="top:110px">Introduction</h2>
  <div class="body-copy" style="top:132px">
    <p>Lorem ipsum dolor sit amet, consectetur adipiscing elit. Mauris auctor elit nec neque dictum ultricies. Suspendisse potenti. Etiam eget orci lorem, a commodo enim.</p>
    <p>Donec massa turpis, pulvinar sit amet luctus at, tempor at lorem. Mauris nec massa augue. Phasellus dictum, metus vel posuere ullamcorper, risus erat vehicula magna, id facilisis orci tellus ac magna. Nam a augue lacus, id tempor lorem.</p>
    <p>Mauris odio nunc, dignissim et fermentum eget, venenatis quis turpis. Phasellus faucibus, ligula id pulvinar adipiscing, tortor erat pretium felis, posuere neque nulla pretium lectus.<br>Nulla facilisi. Donec at suscipit quam. Nulla non tortor orci. Fusce purus sem, rutrum et egestas ac, consequat a mi. Curabitur tincidunt massa eget mauris sagittis ornare imperdiet tortor vulputate.</p>
  </div>
  <div class="body-copy body-copy--column" style="top:299px">
    <p>Aenean blandit eros et neque rhoncus sed tristique ante euismod. Curabitur quis nisi quis mi dapibus faucibus sit amet id enim.</p>
    <p>Ut sed dictum dui. Aenean convallis sagittis ipsum, sed tempor dui ultricies sit amet. Praesent sed erat odio. Duis odio elit, commodo vel luctus non, laoreet at eros. Nullam a mauris metus.</p>
  </div>
  <div class="phone-visual" role="img" aria-label="Mobile phone showing a map of nearby golf courses"></div>
  <svg class="callouts" viewBox="0 0 140 80" aria-hidden="true">
    <g stroke="#e8402a" stroke-width=".5">
      <line x1="10" y1="20" x2="52" y2="32"/>
      <line x1="10" y1="48" x2="55" y2="55"/>
      <line x1="128" y1="24" x2="80" y2="36"/>
    </g>
    <text class="callout-label" x="0" y="18">Your location</text>
    <text class="callout-label" x="0" y="46">Nearby course</text>
    <text class="callout-label" x="112" y="22">Course info</text>
  </svg>
  <div class="tee-visual" role="img" aria-label="Golf ball resting on a tee"></div>
  <footer class="page__footer"><span class="page__footer-tag">Every Green - Every Player</span><span class="page__footer-url">www.teewisehub.com.au</span></footer>
</section>

<section class="page page--benefits">
  <svg class="page__header" viewBox="0 0 338 140" aria-hidden="true">
    <defs>
      <linearGradient id="band3" x1="0" x2="1"><stop offset="0" stop-color="#d4e86a"/><stop offset=".45" stop-color="#8cc63f"/><stop offset="1" stop-color="#6cb33f"/></linearGradient>
    </defs>
    <path d="M0 0H338V100C250 60 150 25 0 6Z" fill="url(#band3)"/>
    <path d="M60 15C170 33 260 72 338 110V122C260 84 170 44 60 15Z" fill="#c9cacc"/>
  </svg>
  <div class="brand"><span class="brand__mark"></span><span class="brand__name">TeewiseHub</span></div>
  <div class="brand__tagline">Every Green - Every Player</div>
  <h2 class="section-title" style="top:133px">Benefits</h2>
  <div class="body-copy body-copy--benefits" style="top:149px">
    <p>Lorem ipsum dolor sit amet, consectetur adipiscing elit. Mauris auctor elit nec neque dictum ultricies. Suspendisse potenti. Etiam eget orci lorem, a commodo enim.</p>
    <ul class="bullet-list">
      <li>Donec massa turpis, pulvinar sit amet luctus at, tempor at lorem.</li>
      <li>Mauris nec massa augue. Phasellus dictum, metus vel posuere ullamcorper, risus erat vehicula magna, id facilisis orci tellus ac magna.</li>
      <li>Nam a augue lacus, id tempor lorem. Mauris odio nunc, dignissim</li>
      <li>et fermentum eget, venenatis quis turpis. Phasellus faucibus,</li>
      <li>ligula id pulvinar adipiscing, tortor erat pretium felis, posuere</li>
      <li>pretium neque nulla pretium lectus.</li>
      <li>Nulla facilisi. Donec at suscipit quam. Nulla non tortor orci.</li>
      <li>Fusce purus sem, rutrum et egestas ac, consequat a mi.</li>
      <li>Curabitur tincidunt massa eget mauris sagittis</li>
      <li>ornare imperdiet tortor vulputate.</li>
    </ul>
    <p>Aenean blandit eros et neque rhoncus sed tristique ante euismod. Curabitur quis nisi quis mi dapibus faucibus sit amet id enim.</p>
    <p>Ut sed dictum dui. Aenean convallis sagittis ipsum, sed tempor dui ultricies sit amet. Praesent sed erat odio. Duis odio elit, commodo vel luctus non, laoreet at eros. Nullam a mauris metus. Aenean blandit eros et neque rhoncus sed tristique ante euismod. Curabitur quis nisi quis mi dapibus faucibus sit amet id enim.</p>
    <p>Ut sed dictum dui. Aenean convallis sagittis ipsum, sed tempor dui ultricies sit amet. Praesent sed erat odio. Duis odio elit, commodo vel luctus non, laoreet at eros. Nullam a mauris metus a</p>
  </div>
  <div class="brand brand--small"><span class="brand__mark"></span><span class="brand__name">TeewiseHub</span></div>
  <div class="tee-visual" role="img" aria-label="Golf ball resting on a tee"></div>
  <footer class="page__footer"><span class="page__footer-tag">Every Green - Every Player</span><span class="page__footer-url">www.teewisehub.com.au</span></footer>
</section>

<div class="page-label" style="left:43px">Document Page 1</div>
<div class="page-label" style="left:426px">Document Page 2</div>
<div class="page-label" style="left:809px">Document Page 3</div>

<section class="signature">
  <svg class="signature__band" width="160" height="60" viewBox="0 0 160 60" aria-hidden="true">
    <defs>
      <linearGradient id="sigband" x1="0" x2="1"><stop offset="0" stop-color="#c5e06a"/><stop offset=".5" stop-color="#8cc63f"/><stop offset="1" stop-color="#6cb33f"/></linearGradient>
    </defs>
    <path d="M40 0H160V30C120 14 85 6 40 0Z" fill="url(#sigband)"/>
    <path d="M50 2C95 8 130 18 160 32V36C130 22 95 10 50 2Z" fill="#c9cacc"/>
  </svg>
  <div class="signature__name">Dov Hallberg</div>
  <div class="brand"><span class="brand__mark"></span><span class="brand__name">TeewiseHub</span></div>
  <div class="brand__tagline">Every Green - Every Player</div>
  <div class="signature__contact">0471 529 318<br>dov@teewisehub.com.au<br>www.teewisehub.com.au</div>
</section>
<div class="signature-label">Email Signature</div>

</body>
</html>
```